Strength Coach Business Card Design Project

I would like a business card design to complement my new logo. I would like the card to be clean, seek and strong!

Target Market(s)

Mostly adults and junior atheletes who are serious about changing their lives.

Industry/Entity Type

Business

Font styles to use
Serif

Colors

Designer to choose colors to be used in the design.

```html
<!DOCTYPE html>
<html lang="en">
<head>
<meta charset="utf-8">
<title>Ironvale Athletics – Business Card</title>
<link href="https://fonts.googleapis.com/css2?family=Tinos:wght@400;700&display=swap" rel="stylesheet">
<style>
  :root {
    --bg: #d9d6d0;
    --panel-top: #4a4a4c;
    --panel-bottom: #343436;
    --figure: #141414;
    --paper: #ffffff;
    --accent: #e0393e;
    --ink: #2f2f31;
    --rule: #8a8a8c;
  }
  * { margin: 0; padding: 0; box-sizing: border-box; }
  html, body { width: 1200px; height: 800px; overflow: hidden; }
  body {
    background: var(--bg);
    font-family: "Tinos", "Times New Roman", serif;
    color: var(--ink);
  }
  .card {
    position: absolute;
    left: 75px; top: 100px;
    width: 1050px; height: 600px;
    background: var(--paper);
    box-shadow: 0 10px 30px rgba(0,0,0,.18);
    overflow: hidden;
  }
  .card-panel {
    position: absolute; left: 0; top: 0;
    width: 500px; height: 600px;
  }
  .card-figure {
    position: absolute;
    left: 70px; top: 110px;
    width: 340px; height: 400px;
    border-radius: 48% 48% 30% 30%;
    background: radial-gradient(ellipse at 50% 45%, var(--figure) 0%, #1e1e1f 60%, rgba(30,30,31,0) 72%);
  }
  .card-info {
    position: absolute;
    left: 560px; top: 70px;
    width: 440px;
  }
  .person-name {
    color: var(--accent);
    font-weight: 700;
    font-size: 30px;
    letter-spacing: 1px;
    text-transform: uppercase;
  }
  .person-title {
    font-weight: 700;
    font-size: 17px;
    margin-top: 2px;
  }
  .brand {
    display: flex; align-items: center; gap: 16px;
    margin-top: 56px;
    padding-bottom: 26px;
    border-bottom: 1.5px solid var(--rule);
  }
  .brand-mark {
    width: 34px; height: 34px;
    background: var(--accent);
    flex: none;
  }
  .brand-name {
    font-weight: 700;
    font-size: 34px;
    line-height: 1.05;
    color: var(--ink);
    text-transform: uppercase;
    letter-spacing: 1px;
  }
  .contact-list {
    list-style: none;
    margin-top: 26px;
  }
  .contact-item {
    display: flex; align-items: center; gap: 14px;
    font-size: 21px;
    line-height: 36px;
  }
  .contact-icon { width: 18px; height: 18px; flex: none; fill: var(--ink); }
  .contact-icon.is-outline { fill: none; stroke: var(--ink); stroke-width: 2; }
</style>
</head>
<body>
  <div class="card">
    <svg class="card-panel" viewBox="0 0 500 600" aria-hidden="true">
      <defs>
        <linearGradient id="panelShade" x1="0" y1="0" x2="1" y2="1">
          <stop offset="0" stop-color="#4a4a4c"/>
          <stop offset="1" stop-color="#343436"/>
        </linearGradient>
      </defs>
      <polygon points="0,0 470,0 470,70 500,90 470,110 470,600 0,600" fill="url(#panelShade)"/>
    </svg>
    <div class="card-figure" role="img" aria-label="Silhouette of a muscular athlete in a lunge, flexing one arm"></div>

    <div class="card-info">
      <p class="person-name">Marcus Reid</p>
      <p class="person-title">Managing Director</p>

      <div class="brand">
        <span class="brand-mark"></span>
        <span class="brand-name">Ironvale<br>Athletics</span>
      </div>

      <ul class="contact-list">
        <li class="contact-item">
          <svg class="contact-icon" viewBox="0 0 24 24"><path d="M6.6 10.8a15.5 15.5 0 0 0 6.6 6.6l2.2-2.2a1 1 0 0 1 1-.25 11.4 11.4 0 0 0 3.6.6 1 1 0 0 1 1 1V20a1 1 0 0 1-1 1A17 17 0 0 1 3 4a1 1 0 0 1 1-1h3.5a1 1 0 0 1 1 1c0 1.25.2 2.45.6 3.6a1 1 0 0 1-.25 1z"/></svg>
          0044 7781 302
        </li>
        <li class="contact-item">
          <svg class="contact-icon is-outline" viewBox="0 0 24 24"><path d="M2 5h20v14H2z M2 5l10 8 10-8"/></svg>
          hello@ironvale.com
        </li>
        <li class="contact-item">
          <svg class="contact-icon is-outline" viewBox="0 0 24 24"><path d="M10 14a5 5 0 0 0 7 0l3-3a5 5 0 0 0-7-7l-1 1M14 10a5 5 0 0 0-7 0l-3 3a5 5 0 0 0 7 7l1-1"/></svg>
          www.ironvale.com
        </li>
        <li class="contact-item">
          <svg class="contact-icon" viewBox="0 0 24 24"><path d="M12 3l10 9h-3v9h-5v-6h-4v6H5v-9H2z"/></svg>
          48 Harbor Lane, Westfield 00000
        </li>
      </ul>
    </div>
  </div>
</body>
</html>
```